Contemporary Media Company with Logo Needs Business Card Design

Need a modern card design for a full service digital media company using the logo included. Also want the info below on the card. Probably list the services on the card back to save space for the front. Want something contemporary to impress prospective clients. You may want to submit both a somewhat more conservative design, and then a more wild one.
General Info: (this phrase need not be on the card)
Tod Parvin
Founder and CEO
949-628-4513
tod@lumavantstudio.example
lumavantstudio.example
Services: (this word need not be on the card)
Content & Experience Strategy
Brand Development
Search Engine Optimization
Website Design
Website Operation
Social Media Integration
Complete Video Solutions
Industry/Entity Type
Business
Contact Information for Business Card
Tod Parvin
Founder and CEO
949-628-4513
tod@lumavantstudio.example
lumavantstudio.example
Brand Development
Website Design
Website Operation
Social Media Integration
Complete Video Solutions
Look and feel

```html
<!DOCTYPE html>
<html lang="en">
<head>
<meta charset="utf-8">
<title>Tod Parvin – Lumavant Studio</title>
<link rel="stylesheet" href="https://fonts.googleapis.com/css2?family=Didact+Gothic&family=Open+Sans:wght@400&display=swap">
<style>
  :root {
    --card-bg: #222826;
    --card-bg-edge: #1b201f;
    --band-bg: #0f1211;
    --accent: #f26a21;
    --text-light: #f4f4f2;
    --brand-grey: #8f9798;
  }
  html, body {
    margin: 0;
    padding: 0;
    width: 1200px;
    height: 686px;
    overflow: hidden;
    background: var(--card-bg-edge);
  }
  .card {
    position: relative;
    width: 1200px;
    height: 686px;
    box-sizing: border-box;
    border: 2px solid #151918;
    background: radial-gradient(ellipse at 55% 40%, #262c2a 0%, var(--card-bg) 55%, var(--card-bg-edge) 100%);
    font-family: "Open Sans", sans-serif;
    overflow: hidden;
  }
  .name-band {
    position: absolute;
    left: 0;
    top: 133px;
    width: 612px;
    height: 164px;
    background: var(--band-bg);
    border-radius: 0 40px 40px 0 / 0 82px 82px 0;
  }
  .person-name {
    position: absolute;
    left: 55px;
    top: 146px;
    margin: 0;
    font-family: "Didact Gothic", sans-serif;
    font-weight: 400;
    font-size: 66px;
    line-height: 1;
    color: var(--accent);
  }
  .person-title {
    position: absolute;
    left: 55px;
    top: 228px;
    margin: 0;
    font-family: "Didact Gothic", sans-serif;
    font-size: 40px;
    letter-spacing: 2px;
    line-height: 1;
    color: var(--text-light);
  }
  .contact-list {
    position: absolute;
    left: 56px;
    top: 526px;
    margin: 0;
    padding: 0;
    list-style: none;
  }
  .contact-item {
    display: flex;
    align-items: center;
    height: 41px;
    font-size: 27px;
    color: var(--text-light);
    letter-spacing: 0.5px;
  }
  .contact-icon {
    width: 34px;
    height: 34px;
    margin-right: 17px;
    flex: none;
  }
  .brand {
    position: absolute;
    right: 56px;
    top: 578px;
    display: flex;
    align-items: center;
  }
  .brand-mark {
    width: 40px;
    height: 40px;
    background: var(--accent);
    margin-right: 18px;
  }
  .brand-name {
    font-family: "Open Sans", sans-serif;
    font-size: 30px;
    letter-spacing: 3px;
    color: var(--brand-grey);
  }
</style>
</head>
<body>
  <main class="card">
    <div class="name-band"></div>
    <h1 class="person-name">Tod Parvin</h1>
    <p class="person-title">Founder and CEO</p>

    <ul class="contact-list">
      <li class="contact-item">
        <svg class="contact-icon" viewBox="0 0 34 34" aria-hidden="true">
          <circle cx="17" cy="17" r="15" fill="none" stroke="#f26a21" stroke-width="2"/>
          <path d="M12 9.5c1-.6 2-.3 2.6.6l1.3 2.2c.5.9.2 1.7-.6 2.3l-.9.6c.6 2 2.3 4 4.3 5l.8-.8c.7-.7 1.6-.8 2.3-.2l2 1.5c.8.6.9 1.6.2 2.4l-1 1.1c-1.2 1.3-3.4 1-5.6-.6-3-2.2-5.6-5.8-6.3-9.2-.4-2 .1-3.6 1-4.3z" fill="none" stroke="#f26a21" stroke-width="1.8" stroke-linejoin="round"/>
        </svg>
        <span class="contact-text">949-628-4513</span>
      </li>
      <li class="contact-item">
        <svg class="contact-icon" viewBox="0 0 34 34" aria-hidden="true">
          <circle cx="17" cy="17" r="15" fill="none" stroke="#f26a21" stroke-width="2"/>
          <rect x="9" y="11.5" width="16" height="11" fill="none" stroke="#f26a21" stroke-width="1.8"/>
          <path d="M9 11.5l8 6.5 8-6.5M9 22.5l5.8-5.5M25 22.5l-5.8-5.5" fill="none" stroke="#f26a21" stroke-width="1.6"/>
        </svg>
        <span class="contact-text">tod@lumavantstudio.example</span>
      </li>
      <li class="contact-item">
        <svg class="contact-icon" viewBox="0 0 34 34" aria-hidden="true">
          <circle cx="17" cy="17" r="15" fill="none" stroke="#f26a21" stroke-width="2"/>
          <text x="17" y="20" text-anchor="middle" font-family="Open Sans, sans-serif" font-size="8" font-style="italic" fill="#f26a21">http://</text>
        </svg>
        <span class="contact-text">lumavantstudio.example</span>
      </li>
    </ul>

    <div class="brand">
      <div class="brand-mark"></div>
      <span class="brand-name">LUMAVANT STUDIO</span>
    </div>
  </main>
</body>
</html>
```